Bright and beautiful business card for a coach

I'm a personal and business coach based in Perth, Australia. I need a business card that whilst subtle and elegant, will stand out and appeal on a table full of cards.

My business name is Tide Mentoring and the business card must represent the warmth and brightness implied in the name, without being gimmicky. It must have a warmth and appeal and be easy to read.

I prefer clean, minimalist designs.

It must align with the feel of my website and socials: https://www.tidementoring.com.au/
https://www.instagram.com/tidementoringau/
https://www.facebook.com/tidementoringau
Updates

Hi Designers Thank you so much for taking the time to submit designs. I wonder if I could have explained myself a little better. Most of the designs that have been submitted look rather formal and many have quite corporate looking embellishments on them (to my eye). I would like softer, warmer, more organic. I’m open to people playing about and being more abstract, using softer embellishments (e.g the line drawing flowers and grasses I’ve used in my socials) incorporating other colours from my palette or like the social icons in my email signature (in PDF), perhaps playing with size/oversize, playing with the bleed. Please don’t be constrained by what I’ve already done, it merely needs to compliment. I’m sorry if I’m not using the right words or have led you astray. I’m no designer, but I’ve done my website, socials, email signature etc all myself (my logo was a design contest) and I was really hoping for my business card to be something more creative than I could have made with a template. Reminder: No black cards/sides please. Thank you 😊

Target Market(s)

Individuals, most likely but not all female. Creative thinkers. Likely professionals.

Industry/Entity Type

Business & Personal Coach

Contact Information for Business Card

(Tide Mentoring Logo) Name: Maren Delsby; Title: Business & Personal Coach; Phone number: +61 (0)438 915307; Email: maren@tidementoring.com.au; Website: https://tidementoring.com.au; Social icons for Facebook, Instagram & LinkedIn: @tidementoringAU. Optional strapline: "A thinking partner to help you cut through the noise"

Font styles to use
Sans Serif

Colors
00AB8E
00BBA5
67D7C9
C6EFE9
E9F9F6
59FF00
82FF00
B8FF75
E3FFCB
F4FFEA
FFC000
F8CF3A
FAE287
FDF2CF
FEFAEE

Requirements
Must have
• Must align with feel of my website and socials. Must have a pop of #FFC000 (possibly whole of one side, or at least a block). Bright or white background. Easy to read.
Nice to have
• Possibly incorporate the sunshine/grass picture I have used in website and socials - will upload.
Should not have
• Must not be black or dark. Not impersonal or corporate looking.

```html
<!DOCTYPE html>
<html lang="en">
<head>
<meta charset="utf-8">
<title>Tide Mentoring – Business Card</title>
<link href="https://fonts.googleapis.com/css2?family=Lato:ital,wght@0,300;0,400;0,700;1,300;1,400;1,700&family=Mrs+Saint+Delafield&display=swap" rel="stylesheet">
<style>
  :root {
    --stage: #2b2b2b;
    --sun: #FFC000;
    --sun-soft: #FFD426;
    --sun-pale: #FAE287;
    --sun-cream: #FDF2CF;
    --sun-ivory: #FEFAEE;
    --ink-warm: #8a5200;
    --white: #ffffff;
    --teal-deep: #00AB8E;
    --teal: #00BBA5;
    --teal-bright: #00D2B4;
    --teal-soft: #67D7C9;
    --teal-pale: #C6EFE9;
    --mint: #E4F8F4;
  }
  * { margin: 0; padding: 0; box-sizing: border-box; }
  html, body { width: 960px; height: 1200px; overflow: hidden; background: var(--stage); }
  body { font-family: "Lato", Arial, sans-serif; position: relative; }

  .card { position: absolute; left: 36px; width: 888px; height: 542px; overflow: hidden; }
  .card__art { position: absolute; inset: 0; width: 100%; height: 100%; }

  /* Front */
  .card--front { top: 45px; background: var(--sun); }
  .brand {
    position: absolute; left: 0; right: 0; top: 248px;
    display: flex; align-items: center; justify-content: center; gap: 16px;
  }
  .brand__dot { width: 22px; height: 22px; border-radius: 50%; background: var(--white); }
  .brand__name {
    font-size: 50px; font-weight: 300; letter-spacing: 3px; color: var(--white); line-height: 1.2;
  }
  .front__web {
    position: absolute; left: 0; right: 0; top: 488px; text-align: center;
    font-size: 26px; font-weight: 300; letter-spacing: 1px; color: var(--ink-warm); line-height: 1.2;
  }

  /* Back */
  .card--back { top: 612px; background: var(--mint); color: var(--teal); }
  .person { position: absolute; left: 86px; top: 112px; }
  .person__name {
    font-family: "Mrs Saint Delafield", cursive;
    font-size: 58px; line-height: 1; color: var(--teal); font-weight: 400;
  }
  .person__title {
    margin-top: 6px; font-size: 23px; font-weight: 700; font-style: italic;
    letter-spacing: -0.4px; color: var(--teal);
  }
  .contacts { position: absolute; left: 88px; top: 262px; list-style: none; }
  .contacts li { display: flex; align-items: center; height: 43px; font-size: 23px; font-weight: 300; }
  .contacts svg { width: 28px; height: 28px; margin-right: 20px; fill: var(--teal); }
  .socials { position: absolute; left: 604px; top: 65px; list-style: none; }
  .socials li { display: flex; align-items: center; height: 44px; font-size: 21px; font-style: italic; }
  .socials .socials__mark {
    width: 18px; height: 18px; border-radius: 50%; background: var(--teal);
    margin: 0 28px 0 10px;
  }
  .strapline {
    position: absolute; left: 225px; width: 580px; top: 460px; text-align: center;
    font-size: 25px; font-weight: 300; font-style: italic; color: var(--teal); line-height: 1.2;
  }
</style>
</head>
<body>

<section class="card card--front">
  <svg class="card__art" viewBox="0 0 888 542" preserveAspectRatio="none">
    <defs>
      <radialGradient id="front-glow-low" cx="0" cy="1" r="1">
        <stop offset="0" stop-color="var(--sun-ivory)"/>
        <stop offset="0.45" stop-color="var(--sun-pale)"/>
        <stop offset="1" stop-color="var(--sun)" stop-opacity="0"/>
      </radialGradient>
      <radialGradient id="front-glow-high" cx="1" cy="0" r="1">
        <stop offset="0" stop-color="var(--sun-ivory)"/>
        <stop offset="0.45" stop-color="var(--sun-pale)"/>
        <stop offset="1" stop-color="var(--sun)" stop-opacity="0"/>
      </radialGradient>
    </defs>
    <rect x="0" y="160" width="400" height="382" fill="url(#front-glow-low)" role="img" aria-label="Soft sun-coloured light washing in from the lower left corner"/>
    <rect x="560" y="0" width="328" height="200" fill="url(#front-glow-high)" role="img" aria-label="Soft sun-coloured light washing in from the upper right corner"/>
  </svg>
  <div class="brand">
    <span class="brand__dot"></span>
    <span class="brand__name">Tide Mentoring</span>
  </div>
  <p class="front__web">www.tidementoring.com.au</p>
</section>

<section class="card card--back">
  <svg class="card__art" viewBox="0 0 888 542" preserveAspectRatio="none">
    <defs>
      <radialGradient id="petal-glow" cx="1" cy="0.75" r="0.9">
        <stop offset="0" stop-color="var(--teal-pale)" stop-opacity="0.9"/>
        <stop offset="1" stop-color="var(--teal-pale)" stop-opacity="0"/>
      </radialGradient>
      <radialGradient id="back-glow-low" cx="0" cy="1" r="1">
        <stop offset="0" stop-color="var(--teal)"/>
        <stop offset="0.5" stop-color="var(--teal-soft)"/>
        <stop offset="1" stop-color="var(--mint)" stop-opacity="0"/>
      </radialGradient>
      <radialGradient id="back-glow-high" cx="1" cy="0" r="1">
        <stop offset="0" stop-color="var(--teal)"/>
        <stop offset="0.5" stop-color="var(--teal-soft)"/>
        <stop offset="1" stop-color="var(--mint)" stop-opacity="0"/>
      </radialGradient>
    </defs>
    <rect x="560" y="100" width="328" height="442" fill="url(#petal-glow)" role="img" aria-label="Soft scattered petal pattern"/>
    <rect x="0" y="330" width="230" height="212" fill="url(#back-glow-low)" role="img" aria-label="Soft teal light washing in from the lower left corner"/>
    <rect x="770" y="0" width="118" height="110" fill="url(#back-glow-high)" role="img" aria-label="Soft teal light washing in from the upper right corner"/>
  </svg>

  <div class="person">
    <h1 class="person__name">Maren Delsby</h1>
    <p class="person__title">Business &amp; Personal Coach</p>
  </div>

  <ul class="contacts">
    <li>
      <svg viewBox="0 0 24 24" aria-hidden="true"><rect x="5" y="1" width="14" height="22" rx="3" transform="rotate(-8 12 12)"/><circle cx="13" cy="18.5" r="1.3" fill="var(--mint)"/></svg>
      +61 (0)438 915307
    </li>
    <li>
      <svg viewBox="0 0 24 24" aria-hidden="true"><rect x="1" y="4" width="22" height="16" rx="2"/><path d="M3 6 L12 13 L21 6" stroke="var(--mint)" stroke-width="2" fill="none"/></svg>
      maren@tidementoring.com.au
    </li>
    <li>
      <svg viewBox="0 0 24 24" aria-hidden="true"><circle cx="12" cy="12" r="10"/><path d="M2 12 H22 M12 2 C8 6 8 18 12 22 M12 2 C16 6 16 18 12 22" stroke="var(--mint)" stroke-width="1.6" fill="none"/></svg>
      www.tidementoring.com.au
    </li>
  </ul>

  <ul class="socials">
    <li><span class="socials__mark"></span>Tide Mentoring</li>
    <li><span class="socials__mark"></span>tidementoringau</li>
    <li><span class="socials__mark"></span>@tidementoringau</li>
  </ul>

  <p class="strapline">«A thinking partner to help you cut through the noise»</p>
</section>

</body>
</html>
```